Design packaging for dumplings for supermarket shelves

I am looking for packaging design for my new dumplings which are to be put onto gourmet super market shelves. My dumplings are ‘fusion’ and made from very high quality ingredients. My flavours are innovated and produced by me.
The brand is luxe and ‘fun’ combined

Please check out my website for the products, logos and things which i would like it to have.

I do have more photos as well as cartoons of the product but I can’t seem to share them over pixel harbor. Please enquire and I can see you a drop box link

Target Market(s)

Consumers who want to have a great product to eat at home and not too worried about cost

Industry/Entity Type

Dumplings

Font styles to use
Other font styles liked:
• See font on website www.rosyparcel.com

Requirements
Must have
• Photos of the dumplings on the front or to have a window where you can see to dumplings inside the package. Must have space for a nutritional panel as well as a drescription
Nice to have
• It would be nice to see decals which can feature some of the ingredients such as ‘Wagyu Beef’ and ‘Victorian Berkshire Pork’

```html
<!DOCTYPE html>
<html lang="en">
<head>
<meta charset="utf-8">
<title>Rosy Parcel – Sui Gao Pack Front</title>
<link rel="stylesheet" href="https://fonts.googleapis.com/css2?family=Didact+Gothic&family=Montserrat:wght@500;600&display=swap">
<style>
  :root {
    --brand-red: #cd5151;
    --cream-yellow: #fde08c;
    --pattern-light: #f1f0f1;
    --pattern-mid: #e9e8e9;
    --window-grey: #e6e4e5;
    --frost-blue: #1b5b8f;
    --ink: #111111;
    --white: #ffffff;
    --page: #ffffff;
  }
  * { margin: 0; padding: 0; box-sizing: border-box; }
  html, body {
    width: 1200px; height: 1200px; overflow: hidden;
    background: var(--page);
  }
  .canvas { position: relative; width: 1200px; height: 1200px; }
  .pack-front {
    position: absolute; left: 230px; top: 83px;
    width: 739px; height: 1045px; overflow: hidden;
    box-shadow: 0 2px 10px rgba(0,0,0,0.12);
  }
  .pack-pattern {
    position: absolute; inset: 0;
    background: radial-gradient(circle at 50% 55%, var(--pattern-light), var(--pattern-mid));
  }
  .top-band { position: absolute; left: 0; top: 0; width: 739px; height: 460px; }
  .tagline {
    position: absolute; left: 0; right: 0; top: 54px;
    text-align: center; color: var(--white);
    font-family: "Didact Gothic", sans-serif; font-size: 33px; letter-spacing: 0.3px;
  }
  .brand-mark {
    position: absolute; left: 269px; top: 176px;
    width: 200px; height: 200px; border-radius: 50%;
    background: var(--cream-yellow); border: 10px solid var(--white);
  }
  .brand-plate {
    position: absolute; left: 214px; top: 378px;
    width: 311px; height: 74px; border-radius: 37px;
    background: var(--brand-red); border: 6px solid var(--white);
    display: flex; align-items: center; justify-content: center;
  }
  .brand-name {
    color: var(--white);
    font-family: "Didact Gothic", sans-serif; font-size: 40px; line-height: 1; letter-spacing: 1.5px;
  }
  .frozen-badge { position: absolute; left: 546px; top: 181px; width: 92px; height: 134px; }
  .origin-tag {
    position: absolute; left: 274px; top: 474px; width: 191px; height: 82px;
    background: var(--cream-yellow); border-radius: 4px;
    text-align: center; color: var(--ink); font-family: "Montserrat", sans-serif;
  }
  .origin-tag .made-in { font-size: 37px; font-weight: 600; line-height: 44px; margin-top: 3px; letter-spacing: 1px; }
  .origin-tag .rule { height: 2px; background: var(--brand-red); margin: 0 9px; }
  .origin-tag .city { font-size: 24px; font-weight: 500; line-height: 30px; letter-spacing: 0.5px; }
  .window-frame { position: absolute; left: 64px; top: 637px; width: 610px; height: 266px; }
  .product-header {
    position: absolute; left: 129px; top: 575px; width: 494px; height: 160px;
    background: var(--brand-red); border-radius: 80px;
    color: var(--white); text-align: center; font-family: "Didact Gothic", sans-serif;
  }
  .product-name { font-family: "Montserrat", sans-serif; font-weight: 500; font-size: 74px; line-height: 80px; margin-top: 10px; letter-spacing: 1px; }
  .product-header .rule { height: 2px; background: var(--white); margin: 3px 72px 6px; }
  .product-desc { font-size: 29.5px; line-height: 29px; }
  .pack-size {
    position: absolute; left: 0; right: 0; top: 910px;
    text-align: center; color: var(--brand-red); font-family: "Montserrat", sans-serif;
  }
  .pack-size .count { font-size: 36px; font-weight: 600; line-height: 44px; letter-spacing: 1px; }
  .pack-size .rule { width: 168px; height: 4px; background: var(--brand-red); margin: 0 auto 4px; }
  .pack-size .weight { font-size: 26px; font-weight: 500; }
</style>
</head>
<body>
<div class="canvas">
  <div class="pack-front">
    <div class="pack-pattern" role="img" aria-label="Light grey background of flowing noodle-like squiggle pattern"></div>

    <svg class="top-band" viewBox="0 0 739 460" aria-hidden="true">
      <path d="M0 0 H739 V292 Q369.5 606 0 292 Z" fill="var(--brand-red)"/>
    </svg>

    <p class="tagline">Dumplifying Australia s Finest Ingredients</p>

    <div class="brand-mark" aria-hidden="true"></div>
    <div class="brand-plate">
      <p class="brand-name">ROSY PARCEL</p>
    </div>

    <svg class="frozen-badge" viewBox="0 0 92 134" role="img" aria-label="Keep frozen at minus 18 degrees Celsius">
      <rect x="0" y="0" width="92" height="134" rx="46" fill="var(--white)"/>
      <rect x="6" y="6" width="80" height="122" rx="40" fill="var(--frost-blue)"/>
      <g stroke="var(--white)" stroke-width="2.4" stroke-linecap="round">
        <line x1="46" y1="14" x2="46" y2="44"/>
        <line x1="33" y1="21.5" x2="59" y2="36.5"/>
        <line x1="33" y1="36.5" x2="59" y2="21.5"/>
        <path d="M41 16 L46 21 L51 16 M41 42 L46 37 L51 42" fill="none"/>
      </g>
      <text x="46" y="58" text-anchor="middle" fill="var(--white)" font-family="Montserrat, sans-serif" font-weight="600" font-size="11">KEEP</text>
      <text x="46" y="70" text-anchor="middle" fill="var(--white)" font-family="Montserrat, sans-serif" font-weight="600" font-size="11">FROZEN</text>
      <rect x="12" y="74" width="68" height="2.5" fill="var(--white)"/>
      <text x="46" y="98" text-anchor="middle" fill="var(--white)" font-family="Montserrat, sans-serif" font-weight="600" font-size="18">-18</text>
      <text x="46" y="113" text-anchor="middle" fill="var(--white)" font-family="Montserrat, sans-serif" font-weight="600" font-size="8">DEGREES °C</text>
    </svg>

    <div class="origin-tag">
      <p class="made-in">MADE IN</p>
      <div class="rule"></div>
      <p class="city">MELBOURNE</p>
    </div>

    <svg class="window-frame" viewBox="0 0 610 266" role="img" aria-label="Clear window showing the dumplings inside">
      <rect x="0" y="0" width="610" height="266" rx="133" fill="var(--brand-red)"/>
      <rect x="13" y="14" width="584" height="238" rx="119" fill="var(--window-grey)"/>
    </svg>

    <div class="product-header">
      <p class="product-name">SUI GAO</p>
      <div class="rule"></div>
      <p class="product-desc">Victorian Berkshire Pork<br>and Prawn Dumpling</p>
    </div>

    <div class="pack-size">
      <p class="count">8 Pieces</p>
      <div class="rule"></div>
      <p class="weight">240g Aprx.</p>
    </div>
  </div>
</div>
</body>
</html>
```